Design of a can of the adaptogenic drink brand "Brivana" (vector)

Please take the cans from the brief and make a print-ready vector with the instructions as in the other photos.

Target Market(s)

Young, upper-middle class athlete

Industry/Entity Type

Agroalimentaire

Colors

Designer to choose colors to be used in the design.

Requirements
Must have
• Adaptogenic flawed water
Nice to have
• Sleek, classy and healthy

```html
<!DOCTYPE html>
<html lang="en">
<head>
<meta charset="utf-8">
<title>Brivana — Can Design</title>
<link rel="stylesheet" href="https://fonts.googleapis.com/css2?family=Oswald:wght@300;400&display=swap">
<style>
  :root {
    --stage-top: #a9acbb;
    --stage-bottom: #e3e6ee;
    --paper: #ffffff;
    --can-blue: #3a9fc4;
    --can-blue-deep: #2a7fa6;
    --can-white: #f4f5f7;
    --silver-light: #e6e8ea;
    --silver-dark: #9a9ea3;
    --ink-blue: #2f7fb4;
    --ink-silver: #c9ced3;
    --band-navy: #024a6b;
  }
  * { margin: 0; padding: 0; box-sizing: border-box; }
  html, body { width: 1200px; height: 2317px; overflow: hidden; background: var(--paper); }
  body { position: relative; font-family: "Oswald", sans-serif; }

  .stage {
    position: absolute; left: 0; top: 0; width: 1200px; height: 1020px;
    background: linear-gradient(180deg, var(--stage-top) 0%, var(--stage-bottom) 100%);
  }
  .flat-row {
    position: absolute; left: 0; top: 1020px; width: 1200px; height: 1120px;
    background: var(--paper);
  }
  .can { position: absolute; width: 345px; height: 870px; }
  .can--stage-left  { left: 195px; top: 80px; }
  .can--stage-right { left: 652px; top: 80px; }
  .can--flat-left   { left: 198px; top: 158px; }
  .can--flat-right  { left: 648px; top: 158px; }

  .can-tagline { font-family: "Oswald", sans-serif; font-weight: 400; font-size: 17px; letter-spacing: 0.3px; }
  .can-brand   { font-family: "Oswald", sans-serif; font-weight: 300; font-size: 104px; letter-spacing: 10px; }
  .can-tm      { font-family: "Oswald", sans-serif; font-weight: 300; font-size: 11px; }
  .can-volume  { font-family: "Oswald", sans-serif; font-weight: 300; font-size: 24px; }

  .brand-band {
    position: absolute; left: 0; top: 2140px; width: 1200px; height: 177px;
    background: var(--band-navy);
    display: flex; align-items: center; justify-content: center;
  }
  .brand-band__name {
    font-family: "Oswald", sans-serif; font-weight: 300; font-size: 76px;
    letter-spacing: 12px; color: var(--ink-silver);
  }
</style>
</head>
<body>

<svg width="0" height="0" style="position:absolute">
  <defs>
    <linearGradient id="silver" x1="0" x2="1" y1="0" y2="0">
      <stop offset="0" stop-color="#8f9398"/>
      <stop offset="0.3" stop-color="#eef0f2"/>
      <stop offset="0.7" stop-color="#c9cdd1"/>
      <stop offset="1" stop-color="#8f9398"/>
    </linearGradient>
    <linearGradient id="blueBody" x1="0" x2="1" y1="0" y2="0">
      <stop offset="0" stop-color="#2f8db3"/>
      <stop offset="0.25" stop-color="#5cbcdc"/>
      <stop offset="0.6" stop-color="#3a9fc4"/>
      <stop offset="1" stop-color="#2a7fa6"/>
    </linearGradient>
    <linearGradient id="whiteBody" x1="0" x2="1" y1="0" y2="0">
      <stop offset="0" stop-color="#d9dbde"/>
      <stop offset="0.3" stop-color="#ffffff"/>
      <stop offset="0.7" stop-color="#f1f2f4"/>
      <stop offset="1" stop-color="#cfd2d6"/>
    </linearGradient>
  </defs>
</svg>

<section class="stage">
  <svg class="can can--stage-left" viewBox="0 0 345 870">
    <rect x="42" y="0" width="261" height="16" rx="4" fill="url(#silver)"/>
    <path d="M42 16 H303 Q345 50 345 110 V820 Q345 870 290 870 H55 Q0 870 0 820 V110 Q0 50 42 16 Z" fill="url(#blueBody)"/>
    <path d="M0 760 H345 V820 Q345 870 290 870 H55 Q0 870 0 820 Z" fill="url(#silver)"/>
    <text class="can-tagline" x="172" y="102" text-anchor="middle" fill="#ffffff">FUNCTIONAL &amp; WELLNESS DRINK</text>
    <text class="can-brand" x="0" y="0" text-anchor="middle" fill="var(--ink-silver)" transform="translate(212 440) rotate(-90)">BRIVANA</text>
    <text class="can-tm" x="222" y="180" fill="#ffffff">TM</text>
    <text class="can-volume" x="172" y="815" text-anchor="middle" fill="#4d5258">12 fl Oz (355 ml)</text>
  </svg>
  <svg class="can can--stage-right" viewBox="0 0 345 870">
    <rect x="42" y="0" width="261" height="16" rx="4" fill="url(#silver)"/>
    <path d="M42 16 H303 Q345 50 345 110 V820 Q345 870 290 870 H55 Q0 870 0 820 V110 Q0 50 42 16 Z" fill="url(#whiteBody)"/>
    <text class="can-tagline" x="172" y="102" text-anchor="middle" fill="var(--ink-blue)">FUNCTIONAL &amp; WELLNESS DRINK</text>
    <text class="can-brand" x="0" y="0" text-anchor="middle" fill="var(--ink-blue)" transform="translate(212 440) rotate(-90)">BRIVANA</text>
    <text class="can-tm" x="222" y="180" fill="#8a8f95">TM</text>
    <text class="can-volume" x="172" y="815" text-anchor="middle" fill="var(--ink-blue)">12 fl Oz (355 ml)</text>
  </svg>
</section>

<section class="flat-row">
  <svg class="can can--flat-left" viewBox="0 0 345 870">
    <rect x="42" y="0" width="261" height="16" rx="4" fill="url(#silver)"/>
    <path d="M42 16 H303 Q345 50 345 110 V820 Q345 870 290 870 H55 Q0 870 0 820 V110 Q0 50 42 16 Z" fill="url(#blueBody)"/>
    <path d="M0 760 H345 V820 Q345 870 290 870 H55 Q0 870 0 820 Z" fill="url(#silver)"/>
    <text class="can-tagline" x="172" y="102" text-anchor="middle" fill="#ffffff">FUNCTIONAL &amp; WELLNESS DRINK</text>
    <text class="can-brand" x="0" y="0" text-anchor="middle" fill="var(--ink-silver)" transform="translate(212 440) rotate(-90)">BRIVANA</text>
    <text class="can-tm" x="222" y="180" fill="#ffffff">TM</text>
    <text class="can-volume" x="172" y="815" text-anchor="middle" fill="#4d5258">12 fl Oz (355 ml)</text>
  </svg>
  <svg class="can can--flat-right" viewBox="0 0 345 870">
    <rect x="42" y="0" width="261" height="16" rx="4" fill="url(#silver)"/>
    <path d="M42 16 H303 Q345 50 345 110 V820 Q345 870 290 870 H55 Q0 870 0 820 V110 Q0 50 42 16 Z" fill="url(#whiteBody)"/>
    <text class="can-tagline" x="172" y="102" text-anchor="middle" fill="var(--ink-blue)">FUNCTIONAL &amp; WELLNESS DRINK</text>
    <text class="can-brand" x="0" y="0" text-anchor="middle" fill="var(--ink-blue)" transform="translate(212 440) rotate(-90)">BRIVANA</text>
    <text class="can-tm" x="222" y="180" fill="#8a8f95">TM</text>
    <text class="can-volume" x="172" y="815" text-anchor="middle" fill="var(--ink-blue)">12 fl Oz (355 ml)</text>
  </svg>
</section>

<footer class="brand-band">
  <span class="brand-band__name">BRIVANA</span>
</footer>

</body>
</html>
```